New Dental Office Needs an Attractive and user friendly Website Designed

I need a website for a new dental office. The Name is Maplecrest Dentistry. I would like a Modern design with a user friendly interface and usability.
I would like a landing page, a page that lists the services we offer: Cosmetic Dentistry, Implants, Dental Hygiene, Emergency Services, Restorations, Dentures
Target Market(s)
Mid to upper class
Industry/Entity Type
Dentistry
Coding
Coded - Design and coding required
Number of Pages Required
1 page
Requirements
Must have
- Landing page that has a scheduling option, Procedures, operating hours, and contact us info
Nice to have
- Appealing design, Soft comforting colors. Easy to navigate page, Modern and professional.

```html
<!DOCTYPE html>
<html lang="en">
<head>
<meta charset="utf-8">
<title>Maplecrest Dentistry</title>
<link href="https://fonts.googleapis.com/css2?family=Montserrat:wght@500;600;700;800&family=PT+Serif:wght@400;700&display=swap" rel="stylesheet">
<style>
:root{
  --blue:#1a73c9;
  --blue-deep:#1560b0;
  --ink:#1c1c1c;
  --body:#4a4a4a;
  --sky:#e3f0fb;
  --sky-soft:#eef6fd;
  --line:#d3d9df;
  --dark:#1b1b1b;
  --white:#ffffff;
}
*{box-sizing:border-box;margin:0;padding:0}
html,body{width:1200px;height:5106px;overflow:hidden}
body{position:relative;background:var(--white);font-family:"PT Serif",serif;color:var(--body)}
.abs{position:absolute}
.sans{font-family:"Montserrat",sans-serif}
.btn{position:absolute;display:inline-flex;align-items:center;justify-content:center;background:var(--blue);color:var(--white);font-family:"Montserrat",sans-serif;font-weight:600;border-radius:20px;letter-spacing:.3px;text-transform:uppercase;white-space:nowrap}
.photo{position:absolute}
.tag{display:inline-block;background:var(--sky);border-radius:14px;padding:2px 14px;font-size:21px;color:var(--ink)}
.section-title{font-family:"Montserrat",sans-serif;font-weight:700;color:var(--ink);font-size:26px;text-align:center}
.rule{position:absolute;left:588px;width:26px;height:3px;background:var(--blue)}
.center-x{left:0;width:1200px;text-align:center}

/* header */
.logo{position:absolute;font-family:"Montserrat",sans-serif;font-weight:600;color:var(--blue);font-size:24px;letter-spacing:.2px;white-space:nowrap}
.nav-item{position:absolute;top:52px;font-family:"Montserrat",sans-serif;font-size:12px;font-weight:500;color:var(--ink);text-transform:uppercase;white-space:nowrap}
.nav-item.active{color:var(--blue);border-top:2px solid var(--blue);padding-top:6px;top:44px}

/* hero */
.hero-title{left:130px;top:178px;font-family:"Montserrat",sans-serif;font-weight:800;font-size:43px;line-height:53px;color:var(--blue);text-transform:uppercase}
.hero-sub{left:130px;top:352px;font-size:19px;line-height:28px;color:var(--ink)}
.trust{left:130px;top:515px;width:445px;height:105px;background:var(--white);border-radius:12px;box-shadow:0 8px 30px rgba(26,115,201,.14)}
.trust .num{position:absolute;left:28px;top:15px;font-size:28px;color:var(--blue)}
.trust p{position:absolute;left:30px;top:56px;width:230px;font-size:11px;line-height:15px;color:var(--ink)}
.avatars{position:absolute;left:276px;top:37px;display:flex}
.avatars span{width:34px;height:34px;border-radius:50%;border:2px solid var(--white);margin-left:-8px;background:linear-gradient(135deg,#6a4a3a,#b88a6e)}

/* about */
.about-label{left:705px;top:712px}
.about-title{left:710px;top:748px;font-family:"Montserrat",sans-serif;font-weight:700;font-size:27px;line-height:36px;color:var(--ink)}
.about-rule{left:712px;top:840px;width:26px;height:3px;background:var(--blue)}
.para{font-size:11.5px;line-height:15px;color:var(--body)}

/* services */
.services{left:0;top:1075px;width:1200px;height:830px;background:linear-gradient(180deg,var(--sky) 0%,var(--sky-soft) 100%)}
.card{position:absolute;width:298px;height:312px;background:var(--white);border-radius:8px;box-shadow:0 6px 22px rgba(20,80,140,.07)}
.card.featured{background:var(--blue)}
.card .icon{position:absolute;left:40px;top:32px;width:80px;height:80px;border-radius:50%;border:2px solid var(--blue);display:flex;align-items:center;justify-content:center}
.card.featured .icon{border-color:var(--white)}
.card h3{position:absolute;left:40px;top:135px;font-family:"Montserrat",sans-serif;font-weight:700;font-size:15.5px;color:var(--ink)}
.card p{position:absolute;left:40px;top:166px;width:220px;font-size:10.5px;line-height:14.5px;color:var(--body)}
.card.featured h3,.card.featured p{color:var(--white)}
.card .more{position:absolute;left:40px;top:258px;width:92px;height:24px;border-radius:14px;background:var(--blue);color:var(--white);font-family:"Montserrat",sans-serif;font-weight:600;font-size:9px;display:flex;align-items:center;justify-content:center}
.card.featured .more{background:var(--white);color:var(--blue)}

/* reasons */
.reason{position:absolute;left:640px;width:420px}
.reason .ic{position:absolute;left:0;top:0;width:72px;height:72px;border-radius:50%;background:var(--blue);display:flex;align-items:center;justify-content:center}
.reason h4{position:absolute;left:98px;top:2px;font-family:"Montserrat",sans-serif;font-weight:700;font-size:14.5px;color:var(--ink)}
.reason p{position:absolute;left:98px;top:26px;width:300px;font-size:10.5px;line-height:14.5px}

/* gallery */
.ba{position:absolute;top:2775px;width:300px;height:320px;overflow:hidden}
.ba .half{position:absolute;top:0;height:100%;width:50%}
.ba .divider{position:absolute;left:149px;top:0;width:2px;height:100%;background:var(--white)}
.ba .handle{position:absolute;left:134px;top:152px;width:32px;height:32px;border-radius:50%;border:2px solid var(--white);background:rgba(255,255,255,.25)}
.ba .lbl{position:absolute;top:8px;font-size:10px;color:var(--white);background:rgba(0,0,0,.28);padding:2px 8px;border-radius:10px}

/* testimonials */
.tcard{position:absolute;top:3340px;height:260px;background:linear-gradient(90deg,var(--white),var(--sky-soft));border-radius:10px;overflow:hidden;box-shadow:0 4px 18px rgba(20,80,140,.06)}
.tcard .tphoto{position:absolute;left:0;top:0;width:220px;height:100%}
.tcard .stars{position:absolute;left:255px;top:22px;color:var(--blue);font-size:13px;letter-spacing:1px}
.tcard .quote{position:absolute;left:255px;top:44px;width:160px;font-size:10.5px;line-height:14.5px}
.tcard .who{position:absolute;left:262px;top:216px;font-size:10.5px;color:var(--ink);text-transform:uppercase}

/* booking form */
.field{position:absolute;height:40px;border:1px solid #c9cdd2;border-radius:6px;background:var(--white);font-size:10.5px;color:var(--body);padding:12px 14px}

/* footer */
.footer{left:0;top:4760px;width:1200px;height:346px;background:var(--dark);color:#d9d9d9}
.footer h5{position:absolute;font-family:"Montserrat",sans-serif;font-weight:600;font-size:12px;color:var(--white)}
.footer .list{position:absolute;font-size:11px;line-height:24px;white-space:nowrap}
.footer .hours{position:absolute;font-size:11px;line-height:18px;white-space:nowrap}
</style>
</head>
<body>

<!-- background glows -->
<div class="abs" style="left:-120px;top:-40px;width:600px;height:500px;background:radial-gradient(circle,rgba(255,232,170,.35),rgba(255,255,255,0) 65%)"></div>
<div class="abs" style="left:1000px;top:-60px;width:360px;height:360px;background:radial-gradient(circle,rgba(120,180,235,.45),rgba(255,255,255,0) 65%)"></div>

<!-- header -->
<header>
  <div class="logo" style="left:130px;top:42px">Maplecrest Dentistry</div>
  <nav>
    <span class="nav-item active" style="left:570px">Home</span>
    <span class="nav-item" style="left:642px">Procedures</span>
    <span class="nav-item" style="left:764px">Financing</span>
    <span class="nav-item" style="left:866px">Contact us</span>
  </nav>
  <div class="btn" style="left:965px;top:42px;width:106px;height:32px;font-size:11px">Book now</div>
</header>

<!-- hero -->
<section class="hero">
  <h1 class="abs hero-title">Cosmetic,<br>Implant and<br>Family Dentistry</h1>
  <p class="abs hero-sub">Comprehensive care for healthy, beautiful<br>smiles at every stage of life.</p>
  <div class="btn" style="left:130px;top:428px;width:223px;height:38px;font-size:12px">Book an appointment</div>
  <div class="abs trust">
    <div class="num">15k</div>
    <p>We are trusted by many satisfied &amp; Happy Customers, be one of them right now</p>
    <div class="avatars"><span></span><span></span><span></span><span></span><span></span></div>
  </div>
  <div class="photo" role="img" aria-label="Smiling woman in a straw sun hat and polka-dot top" style="left:640px;top:140px;width:460px;height:460px;border-radius:50%;background:linear-gradient(160deg,#cfe6f8,#9cc8ee 60%,#6aa9df)"></div>
</section>

<!-- about -->
<section class="about">
  <div class="photo" role="img" aria-label="Patient smiling during a dental check-up" style="left:130px;top:703px;width:253px;height:175px;border-radius:14px;background:linear-gradient(135deg,#e8d3c2,#a8cde9)"></div>
  <div class="photo" role="img" aria-label="Young woman at a dental examination" style="left:231px;top:904px;width:193px;height:116px;border-radius:14px;background:linear-gradient(135deg,#d9c1ae,#7fb3e0)"></div>
  <div class="photo" role="img" aria-label="Smiling couple embracing" style="left:410px;top:720px;width:208px;height:295px;border-radius:14px;background:linear-gradient(160deg,#bfdaf0,#e7d0bc)"></div>
  <div class="abs about-label"><span class="tag">About us</span></div>
  <h2 class="abs about-title">A Modern Approach to<br>Exceptional Dental Care</h2>
  <div class="abs about-rule"></div>
  <p class="abs para" style="left:710px;top:866px;width:365px">We blend gentle chairside care with modern tools so every visit feels calm, clear and unhurried. From routine cleanings to full smile makeovers, our team explains each step, answers every question and plans treatment around your schedule and comfort. Same-week appointments are often available.</p>
  <div class="btn" style="left:710px;top:998px;width:100px;height:26px;font-size:9.5px">Read more</div>
</section>

<!-- services -->
<section class="abs services">
  <h2 class="abs section-title center-x" style="top:47px">Our Services</h2>
  <div class="rule" style="top:98px"></div>

  <div class="card" style="left:130px;top:145px">
    <div class="icon"><svg width="40" height="40" viewBox="0 0 40 40"><path d="M12 8c-5 0-7 5-6 10 1 4 3 6 3 10 0 4 2 6 3 6 2 0 2-6 4-8 2-2 4-2 6 0 2 2 2 8 4 8 1 0 3-2 3-6 0-4 2-6 3-10 1-5-1-10-6-10-3 0-5 2-8 2s-5-2-6-2z" fill="none" stroke="#1a73c9" stroke-width="2"/></svg></div>
    <h3>Cosmetic Dentistry</h3>
    <p>Gentle, personalised treatment planned around your goals, with clear pricing and a calm chair. We explain each option so you can choose with confidence.</p>
    <div class="more">READ MORE</div>
  </div>
  <div class="card featured" style="left:452px;top:145px">
    <div class="icon"><svg width="40" height="40" viewBox="0 0 40 40"><path d="M12 8c-5 0-7 5-6 10 1 4 3 6 3 10 0 4 2 6 3 6 2 0 2-6 4-8 2-2 4-2 6 0 2 2 2 8 4 8 1 0 3-2 3-6 0-4 2-6 3-10 1-5-1-10-6-10-3 0-5 2-8 2s-5-2-6-2z" fill="none" stroke="#fff" stroke-width="2"/></svg></div>
    <div class="photo" role="img" aria-label="Dental implant model held by a dentist" style="left:170px;top:20px;width:106px;height:106px;border-radius:50%;background:linear-gradient(135deg,#f1e4d8,#c8a995)"></div>
    <h3>Implants</h3>
    <p>Gentle, personalised treatment planned around your goals, with clear pricing and a calm chair. We explain each option so you can choose with confidence.</p>
    <div class="more">READ MORE</div>
  </div>
  <div class="card" style="left:775px;top:145px">
    <div class="icon"><svg width="40" height="40" viewBox="0 0 40 40"><path d="M12 8c-5 0-7 5-6 10 1 4 3 6 3 10 0 4 2 6 3 6 2 0 2-6 4-8 2-2 4-2 6 0 2 2 2 8 4 8 1 0 3-2 3-6 0-4 2-6 3-10 1-5-1-10-6-10-3 0-5 2-8 2s-5-2-6-2z" fill="none" stroke="#1a73c9" stroke-width="2"/><circle cx="30" cy="9" r="3" fill="#1a73c9"/></svg></div>
    <h3>Dental Hygiene</h3>
    <p>Gentle, personalised treatment planned around your goals, with clear pricing and a calm chair. We explain each option so you can choose with confidence.</p>
    <div class="more">READ MORE</div>
  </div>

  <div class="card" style="left:130px;top:480px">
    <div class="icon"><svg width="40" height="40" viewBox="0 0 40 40"><rect x="6" y="11" width="28" height="22" rx="3" fill="none" stroke="#1a73c9" stroke-width="2"/><path d="M15 11V7h10v4" fill="none" stroke="#1a73c9" stroke-width="2"/><path d="M20 16v12M14 22h12" stroke="#1a73c9" stroke-width="2.5"/></svg></div>
    <h3>Emergency Services</h3>
    <p>Gentle, personalised treatment planned around your goals, with clear pricing and a calm chair. We explain each option so you can choose with confidence.</p>
    <div class="more">READ MORE</div>
  </div>
  <div class="card" style="left:452px;top:480px">
    <div class="icon"><svg width="40" height="40" viewBox="0 0 40 40"><path d="M12 8c-5 0-7 5-6 10 1 4 3 6 3 10 0 4 2 6 3 6 2 0 2-6 4-8 2-2 4-2 6 0 2 2 2 8 4 8 1 0 3-2 3-6 0-4 2-6 3-10 1-5-1-10-6-10-3 0-5 2-8 2s-5-2-6-2z" fill="none" stroke="#1a73c9" stroke-width="2"/><path d="M20 14v10" stroke="#1a73c9" stroke-width="2"/></svg></div>
    <h3>Restorations</h3>
    <p>Gentle, personalised treatment planned around your goals, with clear pricing and a calm chair. We explain each option so you can choose with confidence.</p>
    <div class="more">READ MORE</div>
  </div>
  <div class="card" style="left:775px;top:480px">
    <div class="icon"><svg width="40" height="40" viewBox="0 0 40 40"><path d="M6 16c0-5 6-8 14-8s14 3 14 8H6z" fill="none" stroke="#1a73c9" stroke-width="2"/><path d="M6 24h28c0 5-6 8-14 8S6 29 6 24z" fill="none" stroke="#1a73c9" stroke-width="2"/><path d="M12 16v8M17 16v8M23 16v8M28 16v8" stroke="#1a73c9" stroke-width="1.5"/></svg></div>
    <h3>Dentures</h3>
    <p>Gentle, personalised treatment planned around your goals, with clear pricing and a calm chair. We explain each option so you can choose with confidence.</p>
    <div class="more">READ MORE</div>
  </div>
</section>

<!-- reasons -->
<section class="reasons">
  <div class="abs" style="left:0;top:1905px;width:535px;height:675px;background:linear-gradient(180deg,#ffffff 0%,#e9eef3 100%);border-top-right-radius:240px"></div>
  <div class="photo" role="img" aria-label="Young woman in a yellow top smiling in a dental chair" style="left:175px;top:2140px;width:372px;height:372px;border-radius:50%;background:linear-gradient(150deg,#e9f2fa,#c9dff1 50%,#e3c76a)"></div>
  <div class="abs center-x" style="top:1955px"><span class="tag">4 Reasons to love us</span></div>
  <h2 class="abs section-title center-x" style="top:2002px">Healthy Smile is a Beautiful Smile</h2>
  <div class="rule" style="top:2060px"></div>

  <div class="reason" style="top:2116px">
    <div class="ic"><svg width="34" height="34" viewBox="0 0 40 40"><path d="M12 8c-5 0-7 5-6 10 1 4 3 6 3 10 0 4 2 6 3 6 2 0 2-6 4-8 2-2 4-2 6 0 2 2 2 8 4 8 1 0 3-2 3-6 0-4 2-6 3-10 1-5-1-10-6-10-3 0-5 2-8 2s-5-2-6-2z" fill="none" stroke="#fff" stroke-width="2"/></svg></div>
    <h4>Outstanding Patient Care</h4>
    <p>Friendly staff, clear answers and careful treatment that puts your comfort first at every visit.</p>
  </div>
  <div class="reason" style="top:2214px">
    <div class="ic"><svg width="34" height="34" viewBox="0 0 40 40"><path d="M8 30h24M12 30V18M20 30V12M28 30V20" stroke="#fff" stroke-width="2.5" fill="none"/></svg></div>
    <h4>Experience &amp; Reputation</h4>
    <p>Friendly staff, clear answers and careful treatment that puts your comfort first at every visit.</p>
  </div>
  <div class="reason" style="top:2309px">
    <div class="ic"><svg width="34" height="34" viewBox="0 0 40 40"><rect x="10" y="6" width="20" height="28" rx="2" fill="none" stroke="#fff" stroke-width="2"/><path d="M15 20l4 4 7-8" stroke="#fff" stroke-width="2.5" fill="none"/></svg></div>
    <h4>Quality &amp; Accreditation</h4>
    <p>Friendly staff, clear answers and careful treatment that puts your comfort first at every visit.</p>
  </div>
  <div class="reason" style="top:2404px">
    <div class="ic"><svg width="34" height="34" viewBox="0 0 40 40"><rect x="6" y="9" width="28" height="19" rx="2" fill="none" stroke="#fff" stroke-width="2"/><path d="M16 33h8M20 28v5" stroke="#fff" stroke-width="2"/></svg></div>
    <h4>Latest Technologies</h4>
    <p>Friendly staff, clear answers and careful treatment that puts your comfort first at every visit.</p>
  </div>
  <div class="btn" style="left:640px;top:2512px;width:196px;height:34px;font-size:11px">Book an appointment</div>
</section>

<!-- gallery -->
<section class="gallery">
  <div class="abs center-x" style="top:2628px"><span class="tag">Photo Gallery</span></div>
  <h2 class="abs section-title center-x" style="top:2672px">Real Patients' Smile Makeovers</h2>
  <div class="rule" style="top:2728px"></div>

  <div class="ba" style="left:130px">
    <div class="half" role="img" aria-label="Close-up smile before whitening" style="left:0;background:linear-gradient(160deg,#d9a98c,#b27b60)"></div>
    <div class="half" role="img" aria-label="Close-up smile after whitening" style="left:50%;background:linear-gradient(160deg,#e4b79b,#c08a6e)"></div>
    <div class="divider"></div><div class="handle"></div>
    <span class="lbl" style="left:8px">Before</span><span class="lbl" style="right:8px">After</span>
  </div>
  <div class="ba" style="left:451px">
    <div class="half" role="img" aria-label="Close-up smile before restoration" style="left:0;background:linear-gradient(160deg,#e8bfb3,#b8503f)"></div>
    <div class="half" role="img" aria-label="Close-up smile after restoration" style="left:50%;background:linear-gradient(160deg,#f0cfc4,#c86352)"></div>
    <div class="divider"></div><div class="handle"></div>
    <span class="lbl" style="left:8px">Before</span><span class="lbl" style="right:8px">After</span>
  </div>
  <div class="ba" style="left:772px">
    <div class="half" role="img" aria-label="Man's smile before treatment" style="left:0;background:linear-gradient(160deg,#5a6e80,#2f3c48)"></div>
    <div class="half" role="img" aria-label="Man's smile after treatment" style="left:50%;background:linear-gradient(160deg,#6a7f90,#3a4855)"></div>
    <div class="divider"></div><div class="handle"></div>
    <span class="lbl" style="left:8px">Before</span><span class="lbl" style="right:8px">After</span>
  </div>

  <div class="abs" style="left:127px;top:3143px;width:946px;height:3px;background:var(--line);border-radius:2px"></div>
  <div class="abs" style="left:127px;top:3142px;width:165px;height:5px;background:var(--blue);border-radius:3px"></div>
  <div class="abs" style="left:283px;top:3135px;width:18px;height:18px;border-radius:50%;background:var(--white);border:3px solid var(--blue)"></div>
  <div class="abs sans" style="left:1033px;top:3137px;width:38px;height:16px;border-radius:8px;background:var(--sky);font-size:9px;color:var(--blue);text-align:center;line-height:16px">1/16</div>
</section>

<!-- testimonials -->
<section class="testimonials">
  <div class="abs center-x" style="top:3190px"><span class="tag">Testimonials</span></div>
  <h2 class="abs section-title center-x" style="top:3240px">What Our Patients Are Saying</h2>
  <div class="rule" style="top:3296px"></div>

  <div class="tcard" style="left:-315px;width:440px">
    <div class="tphoto" role="img" aria-label="Patient portrait" style="background:linear-gradient(135deg,#c9a48c,#7d5a48)"></div>
    <div class="quote">The team made me feel relaxed from the first call. My cleaning was quick and painless, and the results look wonderful. I finally enjoy my visits.</div>
    <div class="who">Olivia Hart</div>
  </div>
  <div class="tcard" style="left:150px;width:440px">
    <div class="tphoto" role="img" aria-label="Smiling woman with curly hair" style="background:linear-gradient(135deg,#d8b69c,#6e4c3c)"></div>
    <div class="stars">★★★★★</div>
    <div class="quote">The team made me feel relaxed from the first call. My cleaning was quick and painless, and the results look wonderful. I finally enjoy my visits.</div>
    <div class="who">Daniel Reyes</div>
  </div>
  <div class="tcard" style="left:617px;width:440px">
    <div class="tphoto" role="img" aria-label="Smiling man in a denim shirt" style="background:linear-gradient(135deg,#c7d8e6,#7b92a8)"></div>
    <div class="stars">★★★★★</div>
    <div class="quote">The team made me feel relaxed from the first call. My cleaning was quick and painless, and the results look wonderful. I finally enjoy my visits.</div>
    <div class="who">Daniel Reyes</div>
  </div>
  <div class="tcard" style="left:1077px;width:440px">
    <div class="tphoto" role="img" aria-label="Smiling woman in a dental chair" style="background:linear-gradient(135deg,#e0c4ae,#7fbfb6)"></div>
    <div class="quote">The team made me feel relaxed from the first call. My cleaning was quick and painless, and the results look wonderful. I finally enjoy my visits.</div>
  </div>

  <svg class="abs" style="left:540px;top:3641px" width="122" height="16" viewBox="0 0 122 16">
    <path d="M8 2 L2 8 L8 14" stroke="#333" stroke-width="1.5" fill="none"/>
    <circle cx="26" cy="8" r="3" fill="#1a73c9"/><circle cx="40" cy="8" r="3" fill="#c9cdd2"/><circle cx="52" cy="8" r="3" fill="#c9cdd2"/><circle cx="64" cy="8" r="3" fill="#c9cdd2"/><circle cx="76" cy="8" r="3" fill="#c9cdd2"/><circle cx="88" cy="8" r="3" fill="#c9cdd2"/>
    <path d="M112 2 L118 8 L112 14" stroke="#333" stroke-width="1.5" fill="none"/>
  </svg>
</section>

<!-- procedures -->
<section class="procedures">
  <div class="photo" role="img" aria-label="Dentist showing a patient her dental scan on a monitor" style="left:553px;top:3725px;width:647px;height:435px;border-top-left-radius:200px;background:linear-gradient(135deg,#2c3a48,#5b7489 55%,#a8bccc)"></div>
  <h2 class="abs sans" style="left:130px;top:3795px;font-weight:700;font-size:27px;color:var(--ink)">Procedures</h2>
  <div class="abs" style="left:130px;top:3838px;width:26px;height:3px;background:var(--blue)"></div>
  <p class="abs para" style="left:130px;top:3860px;width:320px">Our procedures range from preventive cleanings and whitening to implants, crowns and same-day emergency repairs. Every plan starts with a thorough exam and digital imaging, and we review costs, timing and aftercare with you before any work begins.</p>
  <div class="btn" style="left:130px;top:4003px;width:100px;height:27px;font-size:9.5px">Read more</div>
</section>

<!-- booking -->
<section class="booking">
  <div class="abs" style="left:0;top:4170px;width:1200px;height:590px;background:linear-gradient(180deg,#ffffff,#e6f1fb)"></div>
  <h2 class="abs sans center-x" style="top:4230px;font-weight:700;font-size:26px;color:var(--ink);line-height:42px"><span style="background:var(--sky);padding:0 10px;border-radius:8px">Ready to Smile?</span><br>Book Your Appointment Today</h2>
  <div class="rule" style="top:4342px"></div>
  <div class="abs" style="left:130px;top:4395px;width:940px;height:365px;background:var(--white);border-radius:24px 24px 0 0"></div>
  <div class="photo" role="img" aria-label="Woman holding a tooth-shaped mirror in a dental chair" style="left:130px;top:4395px;width:430px;height:365px;border-radius:24px 0 0 0;background:linear-gradient(135deg,#8fd3c9,#e6c7b1 60%,#f2e9e1)"></div>
  <div class="abs" style="left:560px;top:4395px;width:18px;height:365px;background:var(--blue)"></div>
  <div class="field" style="left:625px;top:4442px;width:190px">First Name</div>
  <div class="field" style="left:830px;top:4442px;width:190px">Last Name</div>
  <div class="field" style="left:625px;top:4497px;width:190px">Email id</div>
  <div class="field" style="left:830px;top:4497px;width:190px">Phone</div>
  <div class="field" style="left:625px;top:4552px;width:395px;height:120px">Message</div>
  <div class="btn" style="left:625px;top:4695px;width:104px;height:34px;font-size:13px;border-radius:6px;text-transform:none">Submit</div>
</section>

<!-- footer -->
<footer class="abs footer">
  <div class="logo" style="left:125px;top:52px;color:var(--white);font-size:20px">Maplecrest Dentistry</div>
  <div class="abs" style="left:125px;top:216px;width:290px;height:1px;background:#5a5a5a"></div>
  <h5 style="left:375px;top:55px">Menu</h5>
  <div class="list" style="left:375px;top:80px">Home<br>Procedures<br>Financing<br>Contact us</div>
  <h5 style="left:485px;top:55px">Contact Us</h5>
  <svg class="abs" style="left:490px;top:88px" width="10" height="14" viewBox="0 0 10 14"><path d="M5 0C2 0 0 2 0 5c0 4 5 9 5 9s5-5 5-9c0-3-2-5-5-5z" fill="#fff"/><circle cx="5" cy="5" r="2" fill="#1b1b1b"/></svg>
  <div class="list" style="left:513px;top:84px;line-height:18px">1418 Alder Court<br>Riverton, FL 33410</div>
  <svg class="abs" style="left:490px;top:131px" width="11" height="11" viewBox="0 0 12 12"><path d="M2 0l3 3-2 2c1 2 2 3 4 4l2-2 3 3-2 2C5 12 0 7 0 2z" fill="#fff"/></svg>
  <div class="list" style="left:513px;top:124px">+1 555 010 2040</div>
  <svg class="abs" style="left:490px;top:157px" width="12" height="9" viewBox="0 0 12 9"><rect x="0.5" y="0.5" width="11" height="8" fill="none" stroke="#fff"/><path d="M0.5 0.5l5.5 4 5.5-4" stroke="#fff" fill="none"/></svg>
  <div class="list" style="left:513px;top:148px">hello@maplecrest.example</div>
  <h5 style="left:700px;top:48px">Operating Hours</h5>
  <div class="hours" style="left:700px;top:78px">Monday: 8:00 AM – 5:00 PM<br>Tuesday: 9:00 AM – 6:00 PM<br>Wednesday: 8:00 AM – 5:00 PM<br>Thursday: 9:00 AM – 6:00 PM<br>Friday: 8:00 AM – 2:00 PM<br>Saturday &amp; Sunday: Closed</div>
  <div class="abs" style="left:360px;top:290px;font-size:10px;color:#9a9a9a">Copyright © 2025 All Rights Reserved</div>
  <div class="photo" role="img" aria-label="Smiling woman flossing her teeth" style="left:870px;top:0;width:330px;height:346px;border-top-left-radius:160px;background:linear-gradient(150deg,#5c4a40,#c99a7e 55%,#f1e2d5)"></div>
</footer>

</body>
</html>
```